professional business card

Professional business card with logo on one side, and underneath logo list:
- power
-data
-fibre optic
-isolar

On other side:
Marcus Webb
Owner
MOB 0432 958 720
marcus@vorn.com.au
www.vornelectrical.com.au

Please edit logo to just leave VORN

```html
<!DOCTYPE html>
<html lang="en">
<head>
<meta charset="utf-8">
<title>VORN business card</title>
<link rel="stylesheet" href="https://fonts.googleapis.com/css2?family=Lato:wght@400;700;900&display=swap">
<style>
  :root {
    --teal: #1c9fa3;
    --teal-line: #9fd6d8;
    --ink: #4a4a4a;
    --muted: #6f6f6f;
    --paper: #ffffff;
    --backdrop: #333333;
  }
  * { box-sizing: border-box; margin: 0; padding: 0; }
  html, body { width: 1200px; height: 866px; overflow: hidden; }
  body {
    background: var(--backdrop);
    font-family: "Lato", sans-serif;
    position: relative;
  }
  .card {
    position: absolute;
    top: 270px;
    width: 520px;
    height: 318px;
    overflow: hidden;
    box-shadow: 0 10px 24px rgba(0,0,0,0.45);
  }
  /* Contact side */
  .card--contact { left: 60px; background: var(--paper); }
  .card--contact .edge-band {
    position: absolute; left: 0; right: 0; bottom: 0; height: 10px;
    background: var(--teal);
  }
  .holder { position: absolute; left: 34px; top: 36px; }
  .holder__name {
    color: var(--teal); font-weight: 700; font-size: 20px;
    letter-spacing: 0.5px; text-transform: uppercase;
  }
  .holder__role { color: var(--muted); font-size: 16px; margin-top: 1px; }
  .divider {
    position: absolute; left: 120px; right: 34px; top: 92px;
    height: 1px; background: var(--teal-line);
  }
  .divider--lower { top: 284px; left: 200px; }
  .contact-list {
    position: absolute; left: 34px; top: 104px; list-style: none;
  }
  .contact-list li {
    display: flex; align-items: center; gap: 9px;
    color: var(--ink); font-size: 15px; line-height: 24px;
  }
  .contact-list svg { width: 12px; height: 12px; flex: none; }
  .wordmark {
    position: absolute; right: 36px; top: 186px;
    color: var(--teal); font-weight: 700; font-size: 76px;
    letter-spacing: 5px; line-height: 1;
  }
  /* Brand side */
  .card--brand { left: 620px; background: var(--teal); }
  .brand {
    position: absolute; left: 48px; top: 100px;
  }
  .brand__name {
    color: var(--paper); font-weight: 700; font-size: 96px;
    letter-spacing: 6px; line-height: 1;
  }
  .brand__services {
    color: var(--paper); font-size: 15px; letter-spacing: 0.6px;
    margin-top: 14px; text-transform: uppercase;
  }
</style>
</head>
<body>

<section class="card card--contact" aria-label="Contact side">
  <div class="holder">
    <p class="holder__name">Marcus Webb</p>
    <p class="holder__role">Owner</p>
  </div>
  <div class="divider"></div>
  <ul class="contact-list">
    <li>
      <svg viewBox="0 0 14 14" aria-hidden="true"><path fill="var(--teal)" d="M3 1l2.5 3-1.5 1.5c.8 1.8 2.2 3.2 4 4L9.5 8 13 10.5 11.5 13C6 13 1 8 1 2.5z"/></svg>
      <span>0432 958 720</span>
    </li>
    <li>
      <svg viewBox="0 0 14 14" aria-hidden="true"><rect x="1" y="3" width="12" height="8" fill="var(--teal)"/><path d="M1 3l6 4.5L13 3" stroke="#fff" stroke-width="1.2" fill="none"/></svg>
      <span>marcus@vorn.com.au</span>
    </li>
    <li>
      <svg viewBox="0 0 14 14" aria-hidden="true"><circle cx="7" cy="7" r="6" fill="var(--teal)"/><path d="M1 7h12M7 1c-3 3-3 9 0 12M7 1c3 3 3 9 0 12" stroke="#fff" stroke-width="0.9" fill="none"/></svg>
      <span>www.vornelectrical.com.au</span>
    </li>
  </ul>
  <p class="wordmark">VORN</p>
  <div class="divider divider--lower"></div>
  <div class="edge-band"></div>
</section>

<section class="card card--brand" aria-label="Brand side">
  <div class="brand">
    <p class="brand__name">VORN</p>
    <p class="brand__services">Power | Data | Fibre Optic | Isolar</p>
  </div>
</section>

</body>
</html>
```